Brava Helix Inc - Cutting-Edge Biotech Laboratory - Sleek & Sophisticated

Please design a website that has more of a high-tech and high-end feel, with contents outlined in the uploaded file.

Please have main tabs of the following categories: Home, About, FDA & LAWS, Science, Products, Media, Contact.

Media can include all the videos and photos.

Current website: www.bravahelixlabs.example - it needs to be much more high-end, sleek and more organized. Please do NOT follow the outlines in the old website, but follow the uploaded CONTENT file.

Target Market(s)

doctors

Industry/Entity Type

Biotechnology

Coding

Coded - Design and coding required

Number of Pages Required

5+ page

Requirements
Must have
• Logo
Nice to have
• Some lotion on the website

```html
<!DOCTYPE html>
<html lang="en">
<head>
<meta charset="utf-8">
<title>Brava Helix Inc</title>
<link rel="stylesheet" href="https://fonts.googleapis.com/css2?family=Titillium+Web:wght@300;400;600;700&display=swap">
<style>
:root{
  --red:#e0312b;
  --red-dark:#b81d18;
  --ink:#222;
  --text:#555;
  --muted:#8a8a8a;
  --dark:#2b2b2b;
  --darker:#1e1e1e;
  --line:#e6e6e6;
  --white:#fff;
}
*{box-sizing:border-box;margin:0;padding:0}
html,body{width:1200px;height:4523px;overflow:hidden}
body{position:relative;background:var(--white);font-family:"Titillium Web",Arial,sans-serif;color:var(--text)}
.abs{position:absolute}
.ph{position:absolute}

/* hero */
.hero{left:0;top:0;width:1200px;height:482px;background:radial-gradient(circle at 30% 60%,#f0554a 0%,#c9231c 45%,#8f120e 100%)}
.hero-cell{left:814px;top:0;width:386px;height:482px;background:radial-gradient(circle at 50% 55%,#d9362d 0%,#c22a22 22%,#f2f2f2 40%,#ffffff 70%)}
.brand{display:flex;align-items:center;gap:10px;color:var(--white);font-weight:600;font-size:17px;letter-spacing:.5px}
.brand-dot{width:22px;height:22px;border-radius:50%;background:var(--white)}
.top-brand{left:54px;top:30px}
.top-icons{right:170px;top:38px;display:flex;gap:14px}
.top-icons span{width:14px;height:14px;border-radius:50%;background:var(--red)}
.btn-contact{right:54px;top:33px;background:var(--red);color:var(--white);font-size:12px;padding:4px 12px}
.hero-title{left:150px;top:272px;color:var(--white);font-weight:700;font-size:34px;line-height:1.15}
.hero-sub{left:150px;top:362px;color:var(--white);font-size:17px;font-weight:600}
.hero-dots{left:168px;top:412px;display:flex;gap:7px}
.hero-dots i{width:9px;height:9px;border-radius:50%;border:1px solid var(--white)}
.hero-dots i:first-child{background:var(--white)}

/* nav */
.nav{left:0;top:482px;width:1200px;height:46px;border-bottom:1px solid var(--line)}
.nav ul{position:absolute;left:150px;top:12px;display:flex;gap:36px;list-style:none;font-size:14px;color:var(--ink)}
.nav li.active{border-bottom:2px solid var(--red);padding-bottom:4px}
.search{right:0;top:0;width:380px;height:46px;background:var(--red);color:#ffd7d4;font-size:14px;padding:13px 22px}

/* headings */
.h2{font-weight:300;font-size:36px;color:var(--ink)}

/* about */
.about-text{left:150px;top:655px;width:438px;font-size:12.5px;line-height:1.55}
.about-text p{margin-bottom:14px}
.about-text .lead{color:var(--red);font-weight:600}
.about-text b{color:var(--ink)}
.about-right{left:618px;top:808px;width:440px;font-size:12.5px;line-height:1.55}
.about-right p{margin-bottom:14px}
.thumb{width:135px;height:112px}
.thumb-label{position:absolute;font-size:12px;color:var(--red);font-weight:600}
.ring{position:absolute;border-radius:50%;border:14px solid var(--red)}

/* team */
.team-bg{left:0;top:1266px;width:1200px;height:980px;background:linear-gradient(90deg,#d8d8d8 0%,#f1f1f1 35%,#ffffff 60%)}
.team-bact{left:0;top:1330px;width:420px;height:700px;background:linear-gradient(120deg,#bdbdbd,#e8e8e8 60%,#f4f4f4)}
.team-red{left:648px;top:1327px;width:552px;height:919px;background:var(--red)}
.team-dark{left:300px;top:1600px;width:348px;height:646px;background:var(--dark)}
.photo{position:absolute;width:190px;height:195px;background:linear-gradient(160deg,#9a9a9a,#5a5a5a)}
.photo.blank{background:linear-gradient(160deg,#4a4a4a,#2e2e2e)}
.member{position:absolute;color:var(--white);font-size:13px;line-height:1.35}
.member h3{font-size:20px;font-weight:600;line-height:1.1;margin-bottom:3px}
.member.left{width:116px}
.member.right{width:290px}
.member.on-light{color:var(--ink)}
.pin-dot{position:absolute;width:30px;height:30px;border-radius:50%;border:2px solid var(--red);background:rgba(224,49,43,.35)}

/* research */
.research-title{left:0;top:2282px;width:1200px;text-align:center}
.research-text{left:300px;top:2342px;width:600px;text-align:center;font-size:14px;line-height:1.55;color:var(--ink)}

/* fda */
.fda-dark{left:0;top:2457px;width:730px;height:392px;background:var(--darker)}
.fda-title{left:150px;top:2485px;color:var(--white)}
.fda-label{left:150px;top:2640px;color:var(--white);font-weight:700;font-size:15px}
.fda-text{left:150px;top:2666px;width:245px;color:#cfcfcf;font-size:14px;line-height:1.5}
.card{position:absolute;top:2502px;width:200px;height:296px;background:var(--red);color:var(--white);text-align:center;padding:26px 16px}
.card .icon{width:84px;height:84px;margin:0 auto 26px;border-radius:50%;background:var(--white);display:flex;align-items:center;justify-content:center}
.card h4{font-size:16px;font-weight:600;line-height:1.2;margin-bottom:6px}
.card p{font-size:10.5px;line-height:1.4}

/* media */
.media-title{left:0;top:2884px;width:1200px;text-align:center}
.tile{position:absolute;width:240px;height:241px}
.play{position:absolute;width:46px;height:46px;border-radius:50%;background:var(--red);left:97px;top:97px}
.play:after{content:"";position:absolute;left:18px;top:14px;border-left:14px solid var(--white);border-top:9px solid transparent;border-bottom:9px solid transparent}
.tile-overlay{position:absolute;inset:0;border:6px solid #2b4fb5;background:rgba(224,49,43,.9);color:var(--white);text-align:center;font-size:13px;line-height:1.4;padding:70px 26px}
.tile-overlay small{display:block;margin-top:10px;font-size:10px}
.btn-red{position:absolute;background:var(--red);color:var(--white);font-size:11px;padding:4px 14px}

/* products */
.products-title{left:248px;top:3536px}
.products-intro{left:484px;top:3540px;width:600px;font-size:14px;line-height:1.5;color:var(--ink)}
.product{position:absolute;top:3618px;width:190px;height:212px;background:linear-gradient(180deg,#f7f7f7,#e9e9e9);box-shadow:0 2px 8px rgba(0,0,0,.12)}
.can{position:absolute;left:70px;top:26px;width:52px;height:160px;border-radius:6px;background:linear-gradient(90deg,#8e9aa6,#e6ecf0 45%,#7d8894)}
.product-label{position:absolute;top:3843px;width:190px;text-align:center;font-size:9.5px;color:var(--text);line-height:1.35}
.product-label b{display:block;color:var(--red);font-size:9px}
.dots{position:absolute;left:582px;top:3930px;display:flex;gap:6px}
.dots i{width:7px;height:7px;border-radius:50%;border:1px solid #999}
.dots i:first-child{background:#999}

/* contact */
.contact{left:0;top:4025px;width:1200px;height:498px;background:var(--dark)}
.contact-body{left:845px;top:4000px;width:355px;height:523px;background:radial-gradient(circle at 55% 45%,#f35a4e,#c8231c 55%,#7d0f0b)}
.contact-title{left:150px;top:4056px;color:var(--white);font-weight:700;font-size:36px}
.field{position:absolute;background:var(--darker);color:#9a9a9a;font-size:11px;padding:8px 12px;height:32px}
.info{position:absolute;left:630px;color:#d5d5d5;font-size:11px;line-height:1.35;display:flex;gap:12px}
.info .ico{width:22px;height:22px;border-radius:50%;border:1px solid var(--red);flex:none;display:flex;align-items:center;justify-content:center}
.footer-line{left:0;top:4405px;width:845px;height:1px;background:#444}
.foot-brand{left:150px;top:4426px}
.copyright{left:150px;top:4470px;width:640px;text-align:center;font-size:11px;color:#aaa}
.top-btn{left:770px;top:4466px;width:22px;height:22px;border-radius:50%;border:1px solid var(--red)}
</style>
</head>
<body>

<!-- hero -->
<div class="ph hero" role="img" aria-label="Close-up of red blood cells"></div>
<div class="ph hero-cell" role="img" aria-label="Single red blood cell on white"></div>
<div class="abs brand top-brand"><span class="brand-dot"></span>Brava Helix</div>
<div class="abs top-icons"><span></span><span></span><span></span></div>
<div class="abs btn-contact">Contact us</div>
<h1 class="abs hero-title">Leader in Regenerative Medicine<br>Innovator of the Industry</h1>
<p class="abs hero-sub">Never Compromises on Quality</p>
<div class="abs hero-dots"><i></i><i></i><i></i></div>

<!-- nav -->
<nav class="abs nav">
  <ul>
    <li class="active">Home</li><li>About</li><li>FDA &amp; LAWS</li><li>Media</li><li>Products</li><li>Science</li><li>Contact</li>
  </ul>
  <div class="abs search">Search...</div>
</nav>

<!-- about -->
<h2 class="abs h2" style="left:150px;top:600px">About</h2>
<div class="abs about-text">
  <p><b>Brava Helix Therapy</b> provides non-embryonic stem cells and unique products for doctors in order to help their patients who face major health conditions, as well as those who simply seek to stay young and healthy. Over years of development, we have succeeded by conducting research into major diseases related to kidney, liver and heart failures, and have aided in helping people who have suffered stroke or brain injury to walk or talk again. We have also helped to remove or reverse tumors and to restore physical abilities.</p>
  <p class="lead">Brava Helix Inc is the producer and distributor of the highest quality umbilical cord, amniotic membrane and placental tissue based allografts in the industry. Our innovative products are used for a wide variety of clinical applications including:</p>
</div>
<div class="ph" style="left:618px;top:663px;width:437px;height:127px;background:linear-gradient(120deg,#dfe8ef,#9fc1d9 50%,#e94c6e)" role="img" aria-label="Laboratory test tubes with coloured liquid"></div>
<div class="abs about-right">
  <p>Brava Helix has developed innovative processes and safety protocols, which deliver the highest cell and tissue viability and safety standards. With these safety and quality standards, Brava Helix has become the leader of birth tissue allografts in the field of regenerative medicine.</p>
  <p>Brava Helix's proprietary process preserves the integrity of the birth tissue, thus achieving greater natural outcomes. This unique process yields high concentrations of tissue growth factors, anti-inflammatory cytokines, and structural proteins. Our products contain these extracellular proteins and molecules which promote soft tissue healing, reduce scar tissue, and generate tissue regeneration.</p>
  <p>Our placental tissue recovery process starts when the mother is healthy. Qualified mothers donate their placentas for medical treatments and research. These donors are selected through a strict screening process which includes an extensive patient questionnaire, serological testing and a medical staff interview to ensure donor eligibility. Our proprietary process produces the highest viable tissue stability and the best birth tissue allograft in the industry.</p>
</div>
<div class="ph thumb" style="left:150px;top:970px;background:linear-gradient(135deg,#e8c9b8,#c8463c)" role="img" aria-label="Knee with highlighted joint pain"></div>
<div class="ph thumb" style="left:300px;top:970px;background:linear-gradient(135deg,#6fc7c9,#e06ba8)" role="img" aria-label="Colourful dumbbells"></div>
<div class="ph thumb" style="left:450px;top:970px;background:linear-gradient(135deg,#f2f2f2,#c7352e)" role="img" aria-label="Arm with bandage"></div>
<span class="thumb-label" style="left:150px;top:1090px">Orthopedics</span>
<span class="thumb-label" style="left:300px;top:1090px">Sports Medicine</span>
<span class="thumb-label" style="left:450px;top:1090px">Wound Care</span>
<div class="ph thumb" style="left:150px;top:1125px;background:linear-gradient(135deg,#d8d4cf,#8a8f96)" role="img" aria-label="Foot examination in a clinic"></div>
<div class="ph thumb" style="left:300px;top:1125px;background:linear-gradient(135deg,#1d3f8f,#e05a2a)" role="img" aria-label="Body scan with pain areas highlighted"></div>
<span class="thumb-label" style="left:150px;top:1245px">Podiatry</span>
<span class="thumb-label" style="left:300px;top:1245px">Pain Management</span>
<div class="ring" style="left:-80px;top:1030px;width:190px;height:190px"></div>

<!-- team -->
<div class="ph team-bg"></div>
<div class="ph team-bact" role="img" aria-label="Microscopic view of a bacterium"></div>
<span class="pin-dot" style="left:188px;top:1472px"></span>
<span class="pin-dot" style="left:258px;top:1660px"></span>
<span class="pin-dot" style="left:188px;top:1876px"></span>
<div class="ph team-red"></div>
<div class="ph team-dark"></div>
<h2 class="abs h2" style="left:150px;top:1280px">Team</h2>

<div class="photo" style="left:308px;top:1393px" role="img" aria-label="Portrait of the chief scientist"></div>
<div class="member left on-light" style="left:528px;top:1500px"><h3>Marco Delvane</h3>Chief Scientist</div>
<div class="photo" style="left:678px;top:1393px" role="img" aria-label="Portrait of the project manager"></div>
<div class="member right" style="left:894px;top:1500px"><h3>Nora Vellin</h3>Stem Cell Project Manager</div>

<div class="photo blank" style="left:308px;top:1620px" role="img" aria-label="Portrait placeholder"></div>
<div class="member left" style="left:528px;top:1730px"><h3>Dr. Adrian P. Holt</h3>Holt Center for<br>Cardiac Longevity</div>
<div class="photo" style="left:678px;top:1620px" role="img" aria-label="Portrait of a physician"></div>
<div class="member right" style="left:894px;top:1730px"><h3>Dr. Kurt Fennimore</h3>1906 Orchard Blvd #6,<br>Brookfield TX 77000</div>

<div class="photo blank" style="left:308px;top:1854px" role="img" aria-label="Portrait placeholder"></div>
<div class="member left" style="left:528px;top:1960px"><h3>Dr.<br>Simon Ravell</h3>5807 Linden Rd<br>#175 Fairmont<br>MI 48000</div>
<div class="photo blank" style="left:678px;top:1854px" role="img" aria-label="Portrait placeholder"></div>
<div class="member right" style="left:894px;top:1970px"><h3>Dr. Victor J. Ashdown</h3>Crestline Vascular Care –<br>3740 Ridge Ln #201, Westbrook<br>TX 75000</div>

<!-- research -->
<h2 class="abs h2 research-title">Research</h2>
<p class="abs research-text"><b>Brava Helix Inc</b> is keenly interested in stem cell research, in areas of both laboratory and clinical studies. We strive to in understand the multitude of uses of stem cells and the ideal parameters of such usage. Contact us about possible research partnerships.</p>

<!-- fda -->
<div class="ph fda-dark"></div>
<h2 class="abs h2 fda-title">FDA &amp; Laws</h2>
<svg class="abs" style="left:150px;top:2575px" width="44" height="44" viewBox="0 0 44 44" fill="none" stroke="#fff" stroke-width="2.5">
  <line x1="22" y1="4" x2="22" y2="40"/><line x1="6" y1="10" x2="38" y2="10"/><line x1="12" y1="40" x2="32" y2="40"/>
  <path d="M6 10 L1 24 H11 Z"/><path d="M38 10 L33 24 H43 Z"/>
</svg>
<div class="abs fda-label">FDA</div>
<p class="abs fda-text">Brava Helix is fully compliant of U.S. Food and Drug Administration guidelines issued by the Office of Cellular, Tissue, and Gene Therapies Series.</p>

<div class="card" style="left:416px">
  <div class="icon"><svg width="44" height="44" viewBox="0 0 44 44"><circle cx="22" cy="22" r="12" fill="#e0312b"/><g stroke="#e0312b" stroke-width="3"><line x1="22" y1="2" x2="22" y2="10"/><line x1="22" y1="34" x2="22" y2="42"/><line x1="2" y1="22" x2="10" y2="22"/><line x1="34" y1="22" x2="42" y2="22"/></g></svg></div>
  <h4>"361<sub>"</sub></h4>
  <p>Human Cells, Tissues, and Cellular and Tissue-Based Products <b>(HCT/Ps)</b></p>
  <p style="margin-top:8px"><b>Lena M. Ostrova, MS<br>Division of Human Tissues</b></p>
</div>
<div class="card" style="left:633px">
  <div class="icon"><svg width="44" height="44" viewBox="0 0 44 44" fill="none" stroke="#e0312b" stroke-width="3"><line x1="8" y1="36" x2="34" y2="10"/><rect x="14" y="16" width="20" height="8" transform="rotate(-45 24 20)"/><line x1="32" y1="6" x2="38" y2="12"/></svg></div>
  <h4>What are HCT/Ps?</h4>
  <p>Notes of Tissue Regulation • "361" HCT/Ps<br>Tissue Rules 21 CFR 1271</p>
</div>
<div class="card" style="left:850px">
  <div class="icon"><svg width="44" height="44" viewBox="0 0 44 44" fill="none" stroke="#e0312b" stroke-width="3"><rect x="8" y="8" width="28" height="22"/><line x1="13" y1="15" x2="31" y2="15"/><line x1="13" y1="21" x2="25" y2="21"/><circle cx="30" cy="34" r="5"/></svg></div>
  <h4>Registration</h4>
  <p>Donor Eligibility<br>Current Good Tissue Practice</p>
</div>
<div class="ring" style="left:1140px;top:2745px;width:140px;height:140px"></div>

<!-- media -->
<h2 class="abs h2 media-title">Media</h2>
<div class="tile" style="left:0;top:2955px;background:linear-gradient(135deg,#c9b8a8,#6d5f55)" role="img" aria-label="Therapist treating a patient's back"></div>
<div class="tile" style="left:240px;top:2955px;background:linear-gradient(135deg,#cfd5dc,#7d8793)" role="img" aria-label="Man holding his knee"><span class="play"></span></div>
<div class="tile" style="left:480px;top:2955px;background:linear-gradient(135deg,#e6e6e6,#9ea4aa)" role="img" aria-label="Doctor with a spine model"></div>
<div class="tile" style="left:720px;top:2955px;background:linear-gradient(135deg,#b8b0a8,#5b534e)" role="img" aria-label="Physiotherapist assisting a patient"></div>
<div class="tile" style="left:960px;top:2955px;background:linear-gradient(135deg,#d5d5d5,#434343)" role="img" aria-label="Leg skeleton with knee highlighted"></div>
<div class="tile" style="left:0;top:3196px;background:linear-gradient(135deg,#2b57b8,#e0312b)" role="img" aria-label="Hand x-ray with highlighted joints"></div>
<div class="tile" style="left:240px;top:3196px;background:linear-gradient(135deg,#e8c6b0,#c8463c)" role="img" aria-label="Arm with elbow pain"></div>
<div class="tile" style="left:480px;top:3196px;background:#c23c36" role="img" aria-label="Highlighted media item">
  <div class="tile-overlay">Lorem Ipsum is simply dummy text of the printing and typesetting industry.<small>View More</small></div>
</div>
<div class="tile" style="left:720px;top:3196px;background:linear-gradient(135deg,#3a4650,#a8b4bd)" role="img" aria-label="Doctor reviewing an x-ray"></div>
<div class="tile" style="left:960px;top:3196px;background:linear-gradient(135deg,#d0d0d0,#4d4d4d)" role="img" aria-label="Knee x-ray"><span class="play"></span></div>
<span class="btn-red" style="left:570px;top:3466px">View More</span>

<!-- products -->
<h2 class="abs h2 products-title">Products</h2>
<p class="abs products-intro">Lorem Ipsum has been the industry's standard dummy text ever since the 1500s, when an unknown printer took a galley of type and scrambled it to make a type specimen book.</p>
<div class="product" style="left:250px"><span class="can" role="img" aria-label="Product vial"></span></div>
<div class="product" style="left:482px"><span class="can" role="img" aria-label="Product vial"></span></div>
<div class="product" style="left:714px"><span class="can" role="img" aria-label="Product vial"></span></div>
<div class="product-label" style="left:250px"><b>LOREM IPSUM IS SIMPLY</b>Lorem Ipsum is simply dummy text of the printing and typesetting industry.</div>
<div class="product-label" style="left:482px"><b>LOREM IPSUM IS SIMPLY</b>Lorem Ipsum is simply dummy text of the printing and typesetting industry.</div>
<div class="product-label" style="left:714px"><b>LOREM IPSUM IS SIMPLY</b>Lorem Ipsum is simply dummy text of the printing and typesetting industry.</div>
<div class="dots"><i></i><i></i><i></i><i></i></div>
<span class="btn-red" style="left:570px;top:3966px">See More</span>
<div class="ring" style="left:-90px;top:3738px;width:250px;height:250px"></div>

<!-- contact -->
<div class="ph contact"></div>
<div class="ph contact-body" role="img" aria-label="Anatomical figure showing muscles and skeleton"></div>
<h2 class="abs contact-title">Contact Us</h2>
<div class="field" style="left:150px;top:4130px;width:205px">First Name</div>
<div class="field" style="left:370px;top:4130px;width:220px">Last Name</div>
<div class="field" style="left:150px;top:4180px;width:440px">Email</div>
<div class="field" style="left:150px;top:4230px;width:440px;height:100px">Message</div>
<span class="btn-red" style="left:150px;top:4358px">Submit</span>

<div class="info" style="top:4128px"><span class="ico"><svg width="10" height="12" viewBox="0 0 10 12"><path d="M5 0a4 4 0 0 0-4 4c0 3 4 8 4 8s4-5 4-8a4 4 0 0 0-4-4z" fill="#e0312b"/></svg></span><span>1200 HARBOR CREST ROAD<br>LAKEVIEW HEIGHTS<br>MI 48000</span></div>
<div class="info" style="top:4190px"><span class="ico"><svg width="12" height="9" viewBox="0 0 12 9" fill="none" stroke="#e0312b"><rect x=".5" y=".5" width="11" height="8"/><path d="M.5 .5l5.5 4 5.5-4"/></svg></span><span style="padding-top:4px">info@bravahelixlabs.example</span></div>
<div class="info" style="top:4230px"><span class="ico"><svg width="10" height="10" viewBox="0 0 10 10"><path d="M2 0l2 2-1 2 3 3 2-1 2 2-2 2C4 10 0 6 0 2z" fill="#e0312b"/></svg></span><span>Marco Delvane<br><b style="color:var(--red);font-size:13px">(555) 010-4821</b></span></div>
<div class="info" style="top:4280px"><span class="ico"><svg width="10" height="10" viewBox="0 0 10 10"><path d="M2 0l2 2-1 2 3 3 2-1 2 2-2 2C4 10 0 6 0 2z" fill="#e0312b"/></svg></span><span>Nora Vellin<br><b style="color:var(--red);font-size:13px">(555) 010-6090</b></span></div>

<div class="ph footer-line"></div>
<div class="abs brand foot-brand"><span class="brand-dot"></span>Brava Helix</div>
<p class="abs copyright">Copyright © 2018 Brava Helix. All rights reserved.</p>
<span class="abs top-btn"></span>

</body>
</html>
```